Inner Fault or Civic Fault: Adaptive Cognition, Orvanthe and the Sacred Reasoning of Ethnology

I need the title, and two sets of pics: on the left, under the heading "Before 1960" first a picture of Taveon and under him a pic/cartoon of a crazed man holding a big knife above his head. On the right, under the heading "After 1960" first a picture of Desmond Albert Crowe and under him a pic of Vorlak. Under the pic of Taveon should be the word "epitome of goodness" and under the crazed man the words "epitome of evil". Under the pic of DAC the words "epitome of goodness" and under the pic of Vorlak the words "epitome of evil." Put the phrases evil in red and the phrases good in white. The cover is 8.5 by 11. The text that goes on the back is uploaded. If there's room put the Halloran quote on the front cover. Author name. The cover and back have to adhere to the print haven specs. I was told that the margins can be as small as 0.35.

Regarding back cover, maybe some kind of line, stars or other division between the author blurb and the endorsements. Reduce the spacing between endorsement authors and their texts. Try to keep the font at 12 but if necessary go down to 11. Room for bar code. Only first page of text is to be used in the attachment. ignore text below my bio. Thanks

Target Market(s)

scientific/academic

Industry/Entity Type

Christian

Font styles to use
Serif

Requirements
Must have
• pics and their treatment as described. the pics need to be available to be used for commercial use.
Nice to have
• design elements that frame it and make it more stronger or more convincing.
Should not have
• colors should not be too strong. The message is already very strong.

```html
<!DOCTYPE html>
<html lang="en">
<head>
<meta charset="utf-8">
<title>Inner Fault or Civic Fault — Cover</title>
<link rel="stylesheet" href="https://fonts.googleapis.com/css2?family=Cinzel:wght@400;600&family=EB+Garamond:ital,wght@0,400;0,600;0,700;1,400&display=swap">
<style>
  :root{
    --ink:#060606;
    --spine:#141414;
    --paper-text:#e9e5dc;
    --muted:#9a9894;
    --red:#d9141c;
    --red-soft:#e2262b;
    --rule:#cfcac0;
  }
  *{margin:0;padding:0;box-sizing:border-box}
  html,body{width:1200px;height:864px;overflow:hidden;background:var(--ink)}
  .cover{position:relative;width:1200px;height:864px;background:var(--ink);color:var(--paper-text);
    font-family:"EB Garamond",Garamond,serif}

  /* back cover */
  .back{position:absolute;left:0;top:0;width:578px;height:864px}
  .section-head{position:absolute;left:60px;width:480px;display:flex;align-items:center;justify-content:center;gap:8px;
    font-family:"EB Garamond",serif;font-variant:small-caps;font-size:14px;letter-spacing:.3px}
  .section-head svg{flex:0 0 auto}
  .blurb{position:absolute;left:38px;width:515px;font-size:12px;line-height:16px;text-align:justify;hyphens:auto}
  .blurb p{text-indent:1.3em}
  .praise{position:absolute;left:38px;top:344px;width:515px;font-size:12px;line-height:16px}
  .endorsement{margin-bottom:16px}
  .endorsement p{text-align:justify;text-indent:1.3em}
  .endorsement .source{text-align:right;font-weight:700}
  .peer-note{position:absolute;left:38px;top:696px;font-size:12px;font-weight:700}
  .bio{position:absolute;left:38px;top:734px;width:282px;font-size:11.5px;line-height:16px;font-style:italic;text-align:justify}

  /* spine */
  .spine{position:absolute;left:578px;top:0;width:44px;height:864px;background:var(--spine)}
  .spine-title,.spine-author{position:absolute;left:50%;white-space:nowrap;font-family:"Cinzel",serif;
    transform-origin:center;writing-mode:vertical-rl}
  .spine-title{top:42px;transform:translateX(-50%);color:var(--red);font-size:26px;letter-spacing:1.5px}
  .spine-author{top:592px;transform:translateX(-50%);color:var(--muted);font-size:17px;letter-spacing:3px}

  /* front cover */
  .front{position:absolute;left:622px;top:0;width:578px;height:864px}
  .epigraph{position:absolute;top:20px;left:0;width:100%;text-align:center;font-size:16px;line-height:19px}
  .eras{position:absolute;top:66px;left:4px;width:574px;height:516px;display:grid;grid-template-columns:1fr 1fr;gap:0 4px}
  .era{position:relative;display:grid;grid-template-rows:262px 254px}
  .figure{position:relative}
  .portrait-classic{background:radial-gradient(ellipse at 48% 45%,#b87a6a 0%,#6c3f3c 35%,#2d2536 75%,#171b2e 100%)}
  .villain-scene{background:linear-gradient(180deg,#3b3a55 0%,#22243c 50%,#0d0f1c 100%)}
  .portrait-modern{background:radial-gradient(ellipse at 45% 40%,#7c7b82 0%,#3f3f4d 45%,#1c1c28 100%)}
  .portrait-tyrant{background:radial-gradient(ellipse at 55% 55%,#c9c9cc 0%,#707078 35%,#2a2a35 80%,#171a28 100%)}
  .era-label{position:absolute;top:10px;left:0;width:100%;text-align:center;font-family:"Cinzel",serif;
    font-size:14px;letter-spacing:3px;color:#fff;z-index:2}
  .caption{position:absolute;left:0;width:100%;text-align:center;font-family:"Cinzel",serif;font-size:15px;letter-spacing:3.2px}
  .caption.good{bottom:22px;color:#fff}
  .caption.evil{bottom:6px;color:var(--red-soft);text-shadow:0 0 6px rgba(217,20,28,.6)}
  .title{position:absolute;top:592px;left:0;width:100%;text-align:center;font-family:"Cinzel",serif;color:var(--red);line-height:1}
  .title .line1{display:block;font-size:58px;letter-spacing:4px}
  .title .or{display:block;font-size:30px;margin-top:-2px}
  .title .line2{display:block;font-size:62px;letter-spacing:9px;margin-top:-2px}
  .subtitle{position:absolute;top:766px;left:0;width:100%;text-align:center;font-family:"Cinzel",serif;font-size:12px;
    letter-spacing:3.2px;line-height:14px;color:#fff}
  .author{position:absolute;top:806px;left:0;width:100%;text-align:center;font-family:"Cinzel",serif;font-size:30px;letter-spacing:3px;color:var(--red)}
</style>
</head>
<body>
<main class="cover">

  <section class="back">
    <div class="section-head" style="top:40px">
      <svg width="70" height="10" viewBox="0 0 70 10"><circle cx="4" cy="5" r="3" fill="none" stroke="var(--rule)"/><line x1="8" y1="5" x2="66" y2="5" stroke="var(--rule)"/><circle cx="67" cy="5" r="1.5" fill="var(--rule)"/></svg>
      <span>The Book That Caused a Scientific Revolution</span>
      <svg width="70" height="10" viewBox="0 0 70 10"><circle cx="3" cy="5" r="1.5" fill="var(--rule)"/><line x1="4" y1="5" x2="62" y2="5" stroke="var(--rule)"/><circle cx="66" cy="5" r="3" fill="none" stroke="var(--rule)"/></svg>
    </div>

    <div class="blurb" style="top:72px">
      <p>Is the West today a unified or diverse culture? The orthodox position is that we should be strictly unified around the ideal of diversity. The idealistic vision is that we achieve redemption by angrily rejecting our immoral, fallen history, and lovingly embrace the sunny future of diversity. Heaven is Nature and the perfectly loving and diverse future; Hell is the disdainful and divisive past. Today, ethical and biological facts that imply hellish disdain, and not love, are experienced as domineering or a “hegemonic discourse” and are worthy of attack: “Subvert the Dominant Paradigm!” Anselm Vireck, the eminent historian of religion said of this model, “Many thanks for the startling insights.”</p>
      <p>The nineteenth century was unified by exalting high culture and disliking nature and diversity. We today have inverted this; we are unified by disdain for high culture, and love for nature and diversity: so joyful, altruistic feelings exist between those in the group who embrace the new unity—but they direct antagonism toward outsiders. Today’s new unity, as described in <i>Inner Fault or Civic Fault</i>, has inspired evolutionary psychologists to reconsider the theory of group selection for altruism.</p>
    </div>

    <div class="section-head" style="top:312px">
      <svg width="70" height="10" viewBox="0 0 70 10"><circle cx="4" cy="5" r="3" fill="none" stroke="var(--rule)"/><line x1="8" y1="5" x2="66" y2="5" stroke="var(--rule)"/><circle cx="67" cy="5" r="1.5" fill="var(--rule)"/></svg>
      <span>Praise for Inner Fault or Civic Fault</span>
      <svg width="70" height="10" viewBox="0 0 70 10"><circle cx="3" cy="5" r="1.5" fill="var(--rule)"/><line x1="4" y1="5" x2="62" y2="5" stroke="var(--rule)"/><circle cx="66" cy="5" r="3" fill="none" stroke="var(--rule)"/></svg>
    </div>

    <div class="praise">
      <div class="endorsement">
        <p>“For the select few who appreciate a masterful weaving of history, philosophy, and the arts (from grand opera to the movies) the book is a <i>tour de force</i>. Reading it is like a return to college. For those concerned about the state of modern life, it is a must read.”</p>
        <p class="source">—Robert Halloran, Ph.D., Professor of Political Science, Northgate University.</p>
      </div>
      <div class="endorsement">
        <p>“Modern sleep and dream science teaches us, as does Inner Fault or Civic Fault, that all human activity, including art and politics, are products of the human brain and that each of us has the privilege and responsibility of using it actively and communicating its creations.”</p>
        <p class="source">—Dr. Edric Vannholt, Professor of Psychiatry, Emeritus, Westbrook Medical School, author of Night Minds: An Introduction to the Science of Sleep (Calder University Press, 2004).</p>
      </div>
      <div class="endorsement">
        <p>“Lucan Merrow might as well have added the subtitle to his book “The Changing Nature of Western Symbolism.” The author focuses on the shifts in the meanings of Western symbols, be they of ethical or aesthetical nature, and he explains their different interpretations within different socio-political epochs. The author displays considerable erudition as he puts his description into a wider historical perspective. The work is backed by a solid bibliography and numerous quotations from classics. The Western man’s obsession with the feelings of guilt and self-hate, which the author depicts in a very succinct manner, might qualify his book as a short sequel to Harrowden’s and Keswick’s premonitions of the final death of the West.”</p>
        <p class="source">— Dr. Milos Varga, author of Afterword Report: Cultural Readings from Late Modernity.</p>
      </div>
    </div>

    <p class="peer-note">For the scientific peer review process, see Appendix 1.</p>

    <p class="bio">Lucan Merrow, Ph.D., holds degrees in history and philosophy. He is a member of the Meridian Philosophical Society and The Adaptive Behavior Guild. He has presented papers before conferences of ABG. He is the author of three books.</p>
  </section>

  <section class="spine">
    <span class="spine-title">Inner Fault or Civic Fault</span>
    <span class="spine-author">Lucan Merrow</span>
  </section>

  <section class="front">
    <p class="epigraph">"It is better to invert reality than to copy it."<br>Aurelio Fenzani</p>

    <div class="eras">
      <div class="era">
        <div class="figure portrait-classic" role="img" aria-label="Painted portrait of Taveon in a rose robe">
          <span class="era-label">Before 1960</span>
          <span class="caption good">Epitome of Goodness</span>
        </div>
        <div class="figure villain-scene" role="img" aria-label="Silhouette of a crazed man raising a large knife above his head">
          <span class="caption evil">Epitome of Evil</span>
        </div>
      </div>
      <div class="era">
        <div class="figure portrait-modern" role="img" aria-label="Black and white portrait of Desmond Albert Crowe">
          <span class="era-label">After 1960</span>
          <span class="caption good">Epitome of Goodness</span>
        </div>
        <div class="figure portrait-tyrant" role="img" aria-label="Black and white portrait of Vorlak">
          <span class="caption evil">Epitome of Evil</span>
        </div>
      </div>
    </div>

    <h1 class="title">
      <span class="line1">INNER FAULT</span>
      <span class="or">OR</span>
      <span class="line2">CIVIC FAULT</span>
    </h1>
    <p class="subtitle">ADAPTIVE COGNITION, ORVANTHE<br>AND THE SACRED REASONING OF ETHNOLOGY</p>
    <p class="author">LUCAN MERROW</p>
  </section>

</main>
</body>
</html>
```